Need a book cover design for a Pagelark Book

Book has a long title and sub title so lots of words to fit on the cover.

I can be flexible a bit with the sub title due to the length of it but ideally i can get a design that takes everything.

Here is the title:

Stellar Chemistry: The Roots of Bonding, Catalysis, and Crystal Growth

Sub Title/Heading
An Amateur's Primer on Organic Reactions, Polymer Design, Lattice Science, and Molecular Modelling

```html
<!DOCTYPE html>
<html lang="en">
<head>
<meta charset="utf-8">
<title>Stellar Chemistry — Book Cover</title>
<link rel="stylesheet" href="https://fonts.googleapis.com/css2?family=League+Spartan:wght@700&family=Poppins:wght@600;700&display=swap">
<style>
  :root {
    --backdrop: #a5b1b1;
    --cover-black: #050507;
    --title-blue-a: #1e6fd6;
    --title-blue-b: #4fd8f0;
    --title-pink-a: #c8195a;
    --title-pink-b: #9a4fb8;
    --text-white: #ffffff;
    --accent-orange: #f6a34a;
    --author-cyan: #3fd3f2;
    --art-blue: #2a5fd8;
    --art-magenta: #b02aa8;
    --art-orange: #ff8a2a;
  }
  * { margin: 0; padding: 0; box-sizing: border-box; }
  html, body { width: 1200px; height: 2400px; overflow: hidden; }
  body { background: var(--backdrop); position: relative; }

  .book-cover {
    position: absolute;
    left: 170px; top: 512px;
    width: 860px; height: 1376px;
    background: var(--cover-black);
    overflow: hidden;
    box-shadow: 0 6px 18px rgba(0,0,0,0.35);
    text-align: center;
  }

  .cover-art {
    position: absolute;
    left: 0; top: 440px; width: 100%; height: 936px;
    background:
      radial-gradient(ellipse 260px 200px at 92% 30%, rgba(255,138,42,0.85), rgba(255,138,42,0) 70%),
      radial-gradient(ellipse 340px 260px at 55% 38%, rgba(176,42,168,0.7), rgba(176,42,168,0) 72%),
      radial-gradient(ellipse 300px 240px at 28% 42%, rgba(42,95,216,0.75), rgba(42,95,216,0) 72%),
      radial-gradient(ellipse 500px 260px at 50% 75%, rgba(60,20,80,0.5), rgba(60,20,80,0) 75%),
      linear-gradient(180deg, var(--cover-black) 0%, #0c0818 12%, #0b0716 70%, var(--cover-black) 100%);
  }

  .title {
    position: absolute; left: 0; top: 58px; width: 100%;
    font-family: "League Spartan", sans-serif;
    font-weight: 700;
    line-height: 0.98;
    text-transform: uppercase;
  }
  .title-line {
    display: block;
    -webkit-background-clip: text; background-clip: text;
    color: transparent;
  }
  .title-line--blue {
    font-size: 124px;
    background-image: linear-gradient(100deg, var(--title-blue-a), var(--title-blue-b) 45%, #2a9fe0 70%, var(--title-blue-b));
  }
  .title-line--pink {
    font-size: 112px;
    background-image: linear-gradient(100deg, var(--title-pink-a), #d4405e 50%, var(--title-pink-b));
  }

  .subtitle {
    position: absolute; left: 0; top: 300px; width: 100%;
    font-family: "Poppins", sans-serif;
    font-weight: 700;
    font-size: 38px;
    line-height: 1.28;
    color: var(--text-white);
  }

  .tagline {
    position: absolute; left: 40px; right: 40px; top: 1012px;
    font-family: "Poppins", sans-serif;
    font-weight: 600;
    font-size: 27px;
    line-height: 1.32;
    color: var(--text-white);
  }
  .tagline-accent { color: var(--accent-orange); }

  .author {
    position: absolute; left: 0; top: 1232px; width: 100%;
    font-family: "Poppins", sans-serif;
    font-weight: 700;
    font-size: 52px;
    letter-spacing: 9px;
    color: var(--author-cyan);
  }
</style>
</head>
<body>
  <div class="book-cover">
    <div class="cover-art" role="img" aria-label="Glowing illustration of dark spheres resting on a web of blue, magenta and orange energy lines curving toward a fiery orange ring"></div>

    <h1 class="title">
      <span class="title-line title-line--blue">Stellar</span>
      <span class="title-line title-line--pink">Chemistry</span>
    </h1>

    <p class="subtitle">The Roots of Bonding,<br>Catalysis, and<br>Crystal Growth</p>

    <p class="tagline">
      <span class="tagline-accent">An Amateur's Primer on Organic</span><br>
      Reactions, Polymer Design, Lattice<br>Science, and Molecular Modelling
    </p>

    <p class="author">MARA QUILLET</p>
  </div>
</body>
</html>
```